KVR Brochure

A brochure that depicts what we do here at our personal injury law firm based in California. We help clients that have been involved in motor vehicle accidents, slip and fall, premise liability, wrongful death, and dog bites. We ensure that they obtain quality medical treatment for their injuries that they sustained. We also assist with the repairs to their vehicle and property damage claim at no additional charge. We also specialize in employment law involving wrongful termination, sexual harrasment, hour and wage, labor law violations, etc. We have a website that you can reference www.kvrcounsel-example.com. We are looking for a modern sleek design. Not too much color our office colors are black and white. You can incorporate some burgubndy or dark blue.

```html
<!DOCTYPE html>
<html lang="en">
<head>
<meta charset="utf-8">
<title>KVR Law Group Flyer</title>
<link rel="stylesheet" href="https://fonts.googleapis.com/css2?family=Roboto:ital,wght@0,400;0,500;0,700;1,400;1,500&display=swap">
<style>
  :root {
    --backdrop: #cfcfcf;
    --paper: #ffffff;
    --ink-dark: #0e0e12;
    --ink-dark-2: #2a2326;
    --burgundy: #a11f1b;
    --navy: #1b2637;
    --stone: #c9cccc;
    --text-light: #ffffff;
    --text-dark: #2b2b2b;
  }
  html, body {
    margin: 0;
    width: 1200px;
    height: 2601px;
    overflow: hidden;
    background: var(--backdrop);
    font-family: "Roboto", Arial, sans-serif;
  }
  .flyer {
    position: absolute;
    left: 50px;
    top: 523px;
    width: 1100px;
    height: 1555px;
    box-shadow: 0 6px 18px rgba(0,0,0,.25);
  }
  .paper { fill: var(--paper); }
  .hero-panel { fill: url(#heroGrad); }
  .stone-band { fill: var(--stone); }
  .team-panel { fill: var(--burgundy); }
  .expertise-panel { fill: var(--navy); }
  .portrait { fill: url(#portraitGrad); }
  .team-photo { fill: url(#teamGrad); }
  .team-frame { fill: none; stroke: var(--paper); stroke-width: 2; }
  .cta-pill { fill: var(--burgundy); }
  .rule { fill: var(--paper); }
  .brand-mark { fill: var(--burgundy); }
  .brand-divider { stroke: var(--paper); stroke-width: 2; }
  .brand-name { font: 400 56px "Roboto", Arial, sans-serif; fill: var(--text-light); }
  .firm-name { font: 700 38px "Roboto", Arial, sans-serif; fill: var(--text-light); }
  .firm-tagline { font: italic 500 32px "Roboto", Arial, sans-serif; fill: var(--text-light); }
  .cta-text { font: 700 31px "Roboto", Arial, sans-serif; fill: var(--text-light); }
  .section-title { font: 700 40px "Roboto", Arial, sans-serif; fill: var(--text-light); }
  .team-copy {
    margin: 0;
    font: 400 15.6px/19.4px "Roboto", Arial, sans-serif;
    color: var(--text-light);
    text-align: justify;
  }
  .advice { font: 400 18px "Roboto", Arial, sans-serif; fill: var(--text-dark); }
  .phone { font: 700 38px "Roboto", Arial, sans-serif; fill: var(--burgundy); }
  .website { font: 400 17px "Roboto", Arial, sans-serif; fill: var(--text-dark); }
  .expertise-title { font: 500 27px "Roboto", Arial, sans-serif; fill: var(--text-light); }
  .service { font: 400 17px "Roboto", Arial, sans-serif; fill: var(--text-light); }
  .tick { fill: none; stroke: var(--text-light); stroke-width: 1.8; stroke-linecap: round; stroke-linejoin: round; }
  .closing { font: italic 400 22px "Roboto", Arial, sans-serif; fill: var(--text-light); }
  .closing b { font-weight: 700; }
</style>
</head>
<body>
<svg class="flyer" viewBox="0 0 942 1332" xmlns="http://www.w3.org/2000/svg">
  <defs>
    <linearGradient id="heroGrad" x1="0" y1="0" x2="1" y2="1">
      <stop offset="0" stop-color="#16141a"/>
      <stop offset=".45" stop-color="#2a2326"/>
      <stop offset="1" stop-color="#0b0b0f"/>
    </linearGradient>
    <linearGradient id="portraitGrad" x1="0" y1="0" x2="0" y2="1">
      <stop offset="0" stop-color="#3b302c" stop-opacity="0"/>
      <stop offset=".25" stop-color="#5a4a42"/>
      <stop offset="1" stop-color="#1c1c1f"/>
    </linearGradient>
    <linearGradient id="teamGrad" x1="0" y1="0" x2="0" y2="1">
      <stop offset="0" stop-color="#d9d7d2"/>
      <stop offset=".45" stop-color="#3a3738"/>
      <stop offset="1" stop-color="#141414"/>
    </linearGradient>
    <symbol id="tick" viewBox="0 0 16 16">
      <path class="tick" d="M2 8.5 L6 12.5 L14 3"/>
    </symbol>
  </defs>

  <rect class="paper" width="942" height="1332"/>

  <path class="stone-band" d="M0,860 L451,1130 V1332 H0 Z"/>

  <path class="hero-panel" role="img" aria-label="Dim courtroom background with gavel and scales"
        d="M87,38 H857 Q909,38 909,90 V470 Q909,520 870,545 L420,900 L420,1010 L90,820 Q35,790 35,740 V90 Q35,38 87,38 Z"/>

  <rect class="portrait" role="img" aria-label="Smiling attorney in a dark suit giving a thumbs up"
        x="430" y="180" width="440" height="720" rx="40"/>

  <path class="expertise-panel"
        d="M419,910 L870,575 Q914,545 914,600 V1332 H451 V1215 Q451,1195 435,1185 L419,1175 Z"/>

  <path class="team-panel"
        d="M77,440 Q77,400 108,420 L405,620 Q419,630 419,650 V1180 Q419,1205 395,1190 L115,1000 Q77,975 77,930 Z"/>

  <!-- brand -->
  <rect class="brand-mark" x="72" y="100" width="46" height="46"/>
  <line class="brand-divider" x1="155" y1="78" x2="155" y2="164"/>
  <text class="brand-name" x="176" y="143">Norvale</text>

  <text class="firm-name" x="65" y="237">The KVR Law Group</text>
  <text class="firm-tagline" x="65" y="278">Award-Winning Injury Attorneys</text>

  <rect class="cta-pill" x="65" y="321" width="504" height="52" rx="26"/>
  <text class="cta-text" x="90" y="358">Talk to a Lawyer for FREE Today</text>

  <!-- team -->
  <text class="section-title" x="118" y="542">OUR</text>
  <text class="section-title" x="118" y="590">TEAM</text>
  <rect class="rule" x="118" y="609" width="75" height="5"/>
  <foreignObject x="118" y="638" width="262" height="230">
    <p xmlns="http://www.w3.org/1999/xhtml" class="team-copy">A premier California law firm, the KVR Law Group takes on the powerful to get our clients the justice and compensation they deserve. When tragedy happens, you need an experienced team to navigate the justice system and ensure you receive everything you are entitled to. The award-winning KVR team will work with you and will stand beside you every step of the way.</p>
  </foreignObject>

  <rect class="team-photo" role="img" aria-label="Group photo of the law firm team in dark suits"
        x="116" y="892" width="270" height="226" rx="22"/>
  <rect class="team-frame" x="110" y="886" width="282" height="238" rx="26"/>

  <!-- contact -->
  <text class="advice" x="63" y="1170">FREE Expert Advice.</text>
  <text class="advice" x="63" y="1193">Talk to a Lawyer Today :</text>
  <text class="phone" x="63" y="1250">833.555.0147</text>
  <text class="website" x="63" y="1278">www.kvrcounsel-example.com</text>

  <!-- expertise -->
  <text class="expertise-title" x="874" y="818" text-anchor="end">Our personal injury</text>
  <text class="expertise-title" x="874" y="852" text-anchor="end">law expertise includes</text>
  <rect class="rule" x="800" y="878" width="74" height="5"/>

  <g class="service" text-anchor="end">
    <text x="620" y="943">Burn Injury</text>
    <text x="620" y="975">Dog Bites</text>
    <text x="620" y="1007">Employment Law</text>
    <text x="620" y="1038">Sexual Abuse</text>
    <text x="620" y="1070">Slip and Fall Accidents</text>
    <text x="620" y="1102">Public Utility Litigation</text>
    <text x="846" y="943">Car Accidents</text>
    <text x="846" y="975">Motorcycle Accidents</text>
    <text x="846" y="1007">Truck Accidents</text>
    <text x="846" y="1038">Train Accidents</text>
    <text x="846" y="1070">Rideshare Accidents</text>
    <text x="846" y="1102">Wrongful Death</text>
    <text x="846" y="1133">Product Defects</text>
  </g>
  <g>
    <use href="#tick" x="635" y="930" width="15" height="15"/>
    <use href="#tick" x="635" y="962" width="15" height="15"/>
    <use href="#tick" x="635" y="994" width="15" height="15"/>
    <use href="#tick" x="635" y="1025" width="15" height="15"/>
    <use href="#tick" x="635" y="1057" width="15" height="15"/>
    <use href="#tick" x="635" y="1089" width="15" height="15"/>
    <use href="#tick" x="860" y="930" width="15" height="15"/>
    <use href="#tick" x="860" y="962" width="15" height="15"/>
    <use href="#tick" x="860" y="994" width="15" height="15"/>
    <use href="#tick" x="860" y="1025" width="15" height="15"/>
    <use href="#tick" x="860" y="1057" width="15" height="15"/>
    <use href="#tick" x="860" y="1089" width="15" height="15"/>
    <use href="#tick" x="860" y="1120" width="15" height="15"/>
  </g>

  <text class="closing" x="873" y="1204" text-anchor="end">Need a <tspan font-weight="700">FREE</tspan> second opinion?</text>
  <text class="closing" x="873" y="1232" text-anchor="end">Talk to an experienced lawyer today.</text>
  <text class="closing" x="873" y="1261" text-anchor="end">We are here for you.</text>
</svg>
</body>
</html>
```